Professional Hairdresser needs powerful, clever, simple, modern business card

I need a professional, clever, powerful, bold, attractive, modern/simplistic business card.
I specialize in dimensional hair color, precision haircutting, modern classic design, and signature finishes.
I believe in advanced education, continued training with emphasis on perfect practice, and strive to be the best at what I do.
I am trained by the industry's best and have passion for what I do, I want my business card to reflect my talents, education, capabilities, signature color techniques and design and confidence.
I want to be known as reputable, bold, artistic, aware, classic yet modern, innovative, creative, dimensional, knowledgeable, and educated.
I want something bold, simple, elegant, modern, clever, and legible.
My personal style is progressive, modern, eclectic, clean with modern luxury comfort style.
I love the use of black and white, to creative visual interest and texture. I think putting black as a solid background with white bold font makes the words jump/glow to the eye. I also think a stark white background with bold black fonts looks great, maybe with a punch of red. It is simple, clean, elegant.
I have a QR code I would like to include on the card but have no idea how to make it visually pleasing or make sense.
I do not have a set logo and am not sure if this needs to be done first or if the business card should be done first.

Target Market(s)

Early 20's-mid 60's, female and male, fashion aware, people who can afford my prices, appreciate value

Industry/Entity Type

Training

Requirements
Must have
• I would like to incorporate the QR code I have if possible.
I would like to have my name and contact info.
I would like my logo (or maybe have my logo be RT in a font like listed below).
I would like the fonts to be modern, bold, clean, readable.
Fonts I have looked at are: The font used on the book called: Vexaro A Hundred Years of Hue" I really love. I have looked at glyphvault.example for font and found "Georgiquas", but the designer wanted 200 euros which I just dont have at the time. Others I looked at include "Lin Libertine", Alien-Encounters-solid-regular-italic".
I love font used in the picture I included with the Tobin.Ashcroft ad.
Clean, modern, professional, legible, structured.
Nice to have
• I envision a black background with bold, modern, simple, font in white creating the effect of the words jumping off the card, visually apparent and glowing. Like a really expensive restaurant with a sign that you cant miss because the name is in bright white on black background, simple, bold, modern but not futuristic, powerful, clever, elegant, and draws the eye making it unforgetable. Perhaps layering black and white in order to where the font will be in white.
I see balance and chic.
Perhaps
Should not have
• I appreciate the trends in business design, but realize trends come and go and not sure if having something "trendy" is advisable for me. Having said that, I like creative modern design and sometimes current trends are important in design. I do like red as accent color, the primary blue color, blue on the PixelForum page, the masculine/florescent purple, and the neo bold yellow and the primary color shade of yellow.
I do not want clutter.
I do not want any fonts that are swirly, old-world calligraphy, script, or penmanship style.
I do not want picture of scissors, heads of old-school beauty school hair, or barber poles.

```html
<!DOCTYPE html>
<html lang="en">
<head>
<meta charset="utf-8">
<title>Reid Thorne — Business Card Set</title>
<link href="https://fonts.googleapis.com/css2?family=Bebas+Neue&family=Open+Sans:wght@300;700&display=swap" rel="stylesheet">
<style>
  :root {
    --backdrop: #d9d4cc;
    --sleeve: #262626;
    --sleeve-edge: #1c1c1c;
    --ink-white: #ffffff;
    --hair-violet-1: #b48aa6;
    --hair-violet-2: #8a5a7e;
    --hair-violet-3: #c9a6bd;
    --hair-ash-1: #c4b3a4;
    --hair-ash-2: #8f7e70;
    --hair-ash-3: #d6c8bb;
    --mark-red-1: #b3121a;
    --mark-red-2: #5e0a0e;
    --mark-brown-1: #8d7460;
    --mark-brown-2: #4a3b30;
  }
  * { margin: 0; padding: 0; box-sizing: border-box; }
  html, body { width: 1200px; height: 900px; overflow: hidden; }
  body { background: var(--backdrop); position: relative; font-family: "Open Sans", sans-serif; }

  .card-set { position: absolute; top: 0; width: 300px; height: 900px; }
  .card-set--one { left: 122px; }
  .card-set--two { left: 462px; }
  .card-set--three { left: 812px; }

  .contact-card {
    position: absolute; top: 93px; left: 10px; width: 282px; height: 190px;
    box-shadow: 0 4px 10px rgba(0,0,0,.35);
    overflow: hidden;
  }
  .contact-card__texture { position: absolute; inset: 0; }
  .contact-card--violet .contact-card__texture {
    background: linear-gradient(100deg, var(--hair-violet-3), var(--hair-violet-1) 40%, var(--hair-violet-2) 75%, var(--hair-violet-1));
  }
  .contact-card--ash .contact-card__texture {
    background: linear-gradient(100deg, var(--hair-ash-3), var(--hair-ash-1) 45%, var(--hair-ash-2) 80%, var(--hair-ash-1));
  }
  .contact-card__name {
    position: absolute; top: 22px; left: 30px;
    font-family: "Bebas Neue", sans-serif; font-size: 40px; letter-spacing: 0.5px;
    color: var(--ink-white); line-height: 1;
  }
  .contact-card__list {
    position: absolute; top: 72px; left: 30px; list-style: none;
    color: var(--ink-white); font-weight: 300; font-size: 14px; line-height: 19.5px;
  }
  .contact-card__list li { display: flex; align-items: center; gap: 5px; }
  .contact-card__icon { width: 11px; height: 11px; flex: none; fill: var(--ink-white); }
  .contact-card__icon-letter { font-weight: 700; font-size: 11px; width: 11px; }

  .sleeve {
    position: absolute; top: 270px; left: 0; width: 296px; height: 532px;
    background: radial-gradient(ellipse at 50% 40%, #2d2d2d, var(--sleeve-edge));
    box-shadow: 0 6px 14px rgba(0,0,0,.5);
  }
  .sleeve__mark {
    position: absolute; top: 118px; left: 64px; width: 170px; height: 202px;
    clip-path: polygon(0 0, 100% 0, 100% 100%, 30% 100%, 0 40%);
  }
  .sleeve__mark--red { background: linear-gradient(160deg, var(--mark-red-1), var(--mark-red-2)); }
  .sleeve__mark--brown { background: linear-gradient(160deg, var(--mark-brown-1), var(--mark-brown-2)); }
  .sleeve__wordmark {
    position: absolute; top: 404px; left: 0; width: 100%; text-align: center;
    font-family: "Open Sans", sans-serif; font-weight: 700; font-size: 38px;
    color: var(--ink-white); letter-spacing: -1px;
  }
</style>
</head>
<body>

<section class="card-set card-set--one">
  <article class="contact-card contact-card--violet">
    <div class="contact-card__texture" role="img" aria-label="Violet-tinted hair texture photograph"></div>
    <h1 class="contact-card__name">REIDTHORNE</h1>
    <ul class="contact-card__list">
      <li><svg class="contact-card__icon" viewBox="0 0 12 12"><path d="M2 1h3l1 3-2 1a7 7 0 0 0 3 3l1-2 3 1v3c0 1-1 1-1 1C5 11 1 7 1 2c0 0 0-1 1-1z"/></svg>+239 555 0148</li>
      <li><svg class="contact-card__icon" viewBox="0 0 12 12"><path d="M1 3h10v7H1z M1 3l5 4 5-4" fill="none" stroke="#fff" stroke-width="1.3"/></svg>reid@reidthornepro.example</li>
      <li><span class="contact-card__icon-letter">W</span>reidthornepro.example</li>
      <li><svg class="contact-card__icon" viewBox="0 0 12 12"><circle cx="6" cy="6" r="5.5"/></svg>reidthorne</li>
    </ul>
  </article>
  <div class="sleeve">
    <div class="sleeve__mark sleeve__mark--red" role="img" aria-label="Brand mark area: red hair-texture triangles beside a profile silhouette"></div>
    <p class="sleeve__wordmark">Thorne</p>
  </div>
</section>

<section class="card-set card-set--two">
  <article class="contact-card contact-card--ash">
    <div class="contact-card__texture" role="img" aria-label="Ash-blonde hair texture photograph"></div>
    <h1 class="contact-card__name">REIDTHORNE</h1>
    <ul class="contact-card__list">
      <li><svg class="contact-card__icon" viewBox="0 0 12 12"><path d="M2 1h3l1 3-2 1a7 7 0 0 0 3 3l1-2 3 1v3c0 1-1 1-1 1C5 11 1 7 1 2c0 0 0-1 1-1z"/></svg>+239 555 0148</li>
      <li><svg class="contact-card__icon" viewBox="0 0 12 12"><path d="M1 3h10v7H1z M1 3l5 4 5-4" fill="none" stroke="#fff" stroke-width="1.3"/></svg>reid@reidthornepro.example</li>
      <li><span class="contact-card__icon-letter">W</span>reidthornepro.example</li>
      <li><svg class="contact-card__icon" viewBox="0 0 12 12"><circle cx="6" cy="6" r="5.5"/></svg>reidthorne</li>
    </ul>
  </article>
  <div class="sleeve">
    <div class="sleeve__mark sleeve__mark--brown" role="img" aria-label="Brand mark area: brown hair-texture triangles beside a profile silhouette"></div>
    <p class="sleeve__wordmark">Thorne</p>
  </div>
</section>

<section class="card-set card-set--three">
  <article class="contact-card contact-card--violet">
    <div class="contact-card__texture" role="img" aria-label="Violet-tinted hair texture photograph"></div>
    <h1 class="contact-card__name">REIDTHORNE</h1>
    <ul class="contact-card__list">
      <li><svg class="contact-card__icon" viewBox="0 0 12 12"><path d="M2 1h3l1 3-2 1a7 7 0 0 0 3 3l1-2 3 1v3c0 1-1 1-1 1C5 11 1 7 1 2c0 0 0-1 1-1z"/></svg>+239 555 0148</li>
      <li><svg class="contact-card__icon" viewBox="0 0 12 12"><path d="M1 3h10v7H1z M1 3l5 4 5-4" fill="none" stroke="#fff" stroke-width="1.3"/></svg>reid@reidthornepro.example</li>
      <li><span class="contact-card__icon-letter">W</span>reidthornepro.example</li>
      <li><svg class="contact-card__icon" viewBox="0 0 12 12"><circle cx="6" cy="6" r="5.5"/></svg>reidthorne</li>
    </ul>
  </article>
  <div class="sleeve">
    <div class="sleeve__mark sleeve__mark--red" role="img" aria-label="Brand mark area: red hair-texture triangles beside a profile silhouette"></div>
    <p class="sleeve__wordmark">Thorne</p>
  </div>
</section>

</body>
</html>
```